Commercial Real Estate Executive Recruiting Firm Needs Business Card Design

We need a business card design for BRAMLEY | Executive Recruiting - an executive recruiting firm focused exclusively on the commercial real estate industry. We place professionals ranging from Analyst to the Executive Office covering all investment/finance disciplines (acquisitions, asset management, capital markets, etc.) in all product types (office, retail, multifamily, industrial, land, etc.). We have a passion for helping people (clients and candidates) and have a reputation for being open and honest in our recruiting - and yes, very successful. We have recently developed a new logo and would like to update our business cards as well. I've uploaded some information about our company that contains the new logo.

Target Market(s)

Commercial Real Estate professionals. Primarily in the US. These are typically, smart, driven professionals with finance degrees and MBAs. Primarily men between the ages of 25 and 55.

Industry/Entity Type

Real Estate

Font styles to use
Other font styles liked:
• The font for "BRAMLEY" is Blair ITC (Medium), and "executive recruiting" is Gotham (Book).

Requirements
Must have
• I like the idea of white background on one side and solid color (blue, black, etc.) on back of card.

Would like to utilize the fonts in the logo (to the extent possible) so as to not have too many fonts on card.
Nice to have
• I think the roles (i.e., Acquisitions, Asset Management, etc.,...) is probably likely best placed on the back side of the card with the logo maybe. See attached current business card for content.

```html
<!DOCTYPE html>
<html lang="en">
<head>
<meta charset="utf-8">
<title>BRAMLEY | Executive Recruiting — Business Cards</title>
<link rel="stylesheet" href="https://fonts.googleapis.com/css2?family=Montserrat:wght@400&family=Open+Sans:wght@400&display=swap">
<style>
  :root {
    --stage: #021a3a;
    --card-navy: #0e3a5f;
    --card-white: #ffffff;
    --facade-light: #f3f4f5;
    --facade-mid: #dcdee0;
    --text-light: #ffffff;
    --text-dark: #333333;
    --mark-blue: #2f6ea6;
    --tagline-grey: #6b6b6b;
  }
  * { margin: 0; padding: 0; box-sizing: border-box; }
  html, body { width: 1200px; height: 900px; overflow: hidden; }
  body { background: var(--stage); position: relative; font-family: "Open Sans", sans-serif; }

  .card { position: absolute; overflow: hidden; }

  .card--front {
    left: 61px; top: 51px; width: 690px; height: 397px;
    background: var(--card-navy);
    color: var(--text-light);
  }
  .card--back {
    left: 451px; top: 471px; width: 705px; height: 412px;
    background: var(--card-white);
    color: var(--text-dark);
  }

  .facade {
    position: absolute; inset: 0;
    background:
      linear-gradient(165deg, transparent 0 55%, var(--facade-mid) 55% 100%),
      linear-gradient(100deg, var(--facade-light) 0 40%, var(--card-white) 40% 55%, var(--facade-light) 55% 100%);
    opacity: 0.9;
  }

  .brand { display: flex; align-items: center; gap: 16px; }
  .brand__mark { width: 42px; height: 42px; flex: none; }
  .brand__text { display: flex; flex-direction: column; }
  .brand__name {
    font-family: "Montserrat", sans-serif; font-weight: 400;
    letter-spacing: 3px; line-height: 1;
  }
  .brand__tagline {
    font-family: "Montserrat", sans-serif; font-weight: 400;
    letter-spacing: 1px; line-height: 1; margin-top: 6px;
  }

  .card--front .brand {
    position: absolute; left: 166px; top: 170px;
  }
  .card--front .brand__mark { background: var(--text-light); width: 56px; height: 56px; }
  .card--front .brand__name { font-size: 42px; }
  .card--front .brand__tagline { font-size: 19px; }

  .front__web {
    position: absolute; left: 0; right: 0; top: 244px;
    text-align: center; font-size: 29px; letter-spacing: 0.2px;
  }

  .card--back .brand {
    position: absolute; right: 56px; top: 32px; gap: 12px;
  }
  .card--back .brand__mark { background: var(--mark-blue); width: 44px; height: 44px; }
  .card--back .brand__name { font-size: 29px; color: var(--text-dark); }
  .card--back .brand__tagline { font-size: 14px; color: var(--tagline-grey); margin-top: 4px; }

  .contact {
    position: absolute; right: 57px; top: 260px;
    text-align: right; font-size: 18.5px; line-height: 26px;
    list-style: none;
  }
</style>
</head>
<body>
  <section class="card card--front" aria-label="Card front">
    <div class="brand">
      <span class="brand__mark" aria-hidden="true"></span>
      <div class="brand__text">
        <span class="brand__name">BRAMLEY</span>
        <span class="brand__tagline">executive recruiting</span>
      </div>
    </div>
    <p class="front__web">www.bramleyrecruiting.com</p>
  </section>

  <section class="card card--back" aria-label="Card back">
    <div class="facade" role="img" aria-label="Faint light grey building facade graphic across the card"></div>
    <div class="brand">
      <span class="brand__mark" aria-hidden="true"></span>
      <div class="brand__text">
        <span class="brand__name">BRAMLEY</span>
        <span class="brand__tagline">executive recruiting</span>
      </div>
    </div>
    <ul class="contact">
      <li>1847 Larkspur Avenue</li>
      <li>Plano, Texas 75024</li>
      <li>Phone 214-555-0147</li>
      <li>www.bramleyrecruiting.com</li>
    </ul>
  </section>
</body>
</html>
```